Pelmora Swifts Stridefair - 2 posters

We need two community event posters for an annual marathon with continuity in design showcasing the clubs logo colours and community spirit. Poster one is for the Juniors division which needs to look like a fun day encouraging families to come down and register and compete. It will be distributed to all the schools and social media. Poster two is for the main event again attracting registration with prizes. Encouraging all levels of runners from professionals to amateurs family friendly. It is in a unique location along the city's foreshore with amazing views.

Target Market(s)

Marathon runners, juniors, community and families

Requirements
Must have
• photos, logos details
Nice to have
• We are looking for a motivating high energy poster to entice registration and feel like fun event for the whole comminty

```html
<!DOCTYPE html>
<html lang="en">
<head>
<meta charset="utf-8">
<title>Pelmora Swifts Stridefair Poster</title>
<link rel="stylesheet" href="https://fonts.googleapis.com/css2?family=Montserrat:wght@600;700;800;900&family=Oswald:wght@500;600&display=swap">
<style>
  :root {
    --navy: #123f6e;
    --deep: #0c2f57;
    --blue: #1b5c9a;
    --orange: #f0821f;
    --teal: #2bb3c0;
    --white: #ffffff;
    --page: #e9ebee;
    --ink: #1a1a1a;
  }
  html, body { margin: 0; padding: 0; width: 1200px; height: 1200px; overflow: hidden; background: var(--page); }
  .poster { position: absolute; left: 138px; top: 0; width: 924px; height: 1200px; background: var(--white); overflow: hidden; font-family: "Montserrat", sans-serif; }
  .poster-art { position: absolute; inset: 0; }
  .abs { position: absolute; }
  .club-badge { left: 327px; top: 22px; width: 270px; height: 270px; border-radius: 50%; background: var(--white); border: 9px solid var(--orange); box-sizing: border-box; box-shadow: 0 4px 10px rgba(0,0,0,.25); display: flex; flex-direction: column; align-items: center; justify-content: center; gap: 14px; }
  .club-badge .dot { width: 62px; height: 62px; border-radius: 50%; background: var(--teal); }
  .club-badge .club-name { font-family: "Oswald", sans-serif; font-weight: 600; font-size: 30px; line-height: 1.05; color: var(--navy); text-align: center; text-transform: uppercase; }
  .event-title { left: 0; width: 924px; top: 302px; text-align: center; font-weight: 800; font-size: 33px; color: var(--navy); letter-spacing: .5px; }
  .session { top: 355px; width: 342px; }
  .session.junior { left: 96px; }
  .session.main { left: 487px; }
  .session h3 { margin: 0 0 6px 18px; font-family: "Oswald", sans-serif; font-weight: 500; font-size: 28px; color: var(--ink); text-transform: uppercase; white-space: nowrap; }
  .session.main h3 { font-size: 26px; margin-top: 3px; }
  .pill { display: flex; height: 40px; border-radius: 20px; overflow: hidden; background: var(--navy); font-family: "Oswald", sans-serif; font-weight: 500; font-size: 25px; color: var(--white); }
  .pill .when { flex: 1; display: flex; align-items: center; justify-content: center; }
  .pill .day { width: 124px; background: var(--orange); border-radius: 20px; display: flex; align-items: center; justify-content: center; }
  .divider { left: 461px; top: 362px; width: 3px; height: 86px; background: var(--navy); }
  .distances { left: 0; width: 924px; top: 464px; text-align: center; font-weight: 800; font-size: 19px; color: #d2701a; letter-spacing: .5px; }
  .challenge { left: 112px; top: 843px; width: 276px; height: 276px; border-radius: 50%; background: radial-gradient(circle at 50% 40%, var(--blue), var(--deep)); border: 10px solid var(--orange); box-sizing: border-box; box-shadow: 0 0 0 5px var(--white); display: flex; flex-direction: column; align-items: center; justify-content: center; text-align: center; color: var(--white); font-weight: 700; font-size: 15px; line-height: 1.15; }
  .challenge .prize { font-weight: 800; font-size: 36px; color: var(--orange); margin: 4px 0; }
  .prizes-head { left: 430px; top: 1022px; color: var(--white); font-weight: 800; font-size: 21px; line-height: 1.05; }
  .prizes-head span { display: block; font-size: 34px; }
  .prizes-rule { left: 570px; top: 995px; width: 2px; height: 110px; background: var(--white); }
  .prize-list { left: 584px; top: 996px; margin: 0; padding: 0; list-style: none; color: var(--white); font-weight: 700; font-size: 14px; line-height: 17px; }
  .prize-list b { color: var(--orange); }
  .footer-sponsors { left: 0; top: 1127px; width: 540px; height: 73px; display: flex; align-items: center; gap: 22px; padding-left: 28px; box-sizing: border-box; }
  .footer-sponsors .label { font-weight: 800; font-size: 16px; color: var(--ink); padding-right: 18px; border-right: 2px solid var(--ink); }
  .sponsor { display: flex; align-items: center; gap: 6px; font-weight: 800; font-size: 17px; color: var(--navy); }
  .sponsor i { width: 14px; height: 14px; border-radius: 50%; background: var(--orange); display: inline-block; }
  .register { left: 592px; top: 1136px; color: var(--white); font-weight: 600; font-size: 19px; line-height: 24px; }
  .register strong { display: block; color: var(--deep); font-weight: 800; font-size: 20px; }
</style>
</head>
<body>
<main class="poster">
  <svg class="poster-art" viewBox="0 0 924 1200" width="924" height="1200" aria-hidden="true">
    <defs>
      <linearGradient id="topBand" x1="0" y1="0" x2="1" y2="0">
        <stop offset="0" stop-color="#0c2f57"/><stop offset=".5" stop-color="#1b5c9a"/><stop offset="1" stop-color="#0c2f57"/>
      </linearGradient>
      <linearGradient id="lowerBand" x1="0" y1="0" x2="1" y2="1">
        <stop offset="0" stop-color="#0c2f57"/><stop offset=".6" stop-color="#1b5c9a"/><stop offset="1" stop-color="#123f6e"/>
      </linearGradient>
      <linearGradient id="crowd" x1="0" y1="0" x2="0" y2="1">
        <stop offset="0" stop-color="#d9dee6"/><stop offset=".35" stop-color="#8a7a70"/><stop offset=".7" stop-color="#4a4a52"/><stop offset="1" stop-color="#6f7a3e"/>
      </linearGradient>
    </defs>
    <rect width="924" height="170" fill="url(#topBand)"/>
    <path d="M0,92 Q462,55 924,92 L924,128 Q462,80 0,118 Z" fill="var(--orange)"/>
    <path d="M0,124 Q250,92 560,100 Q250,110 0,148 Z" fill="var(--teal)"/>
    <path d="M0,112 Q462,68 924,118 L924,1200 L0,1200 Z" fill="var(--white)"/>
    <rect x="0" y="510" width="924" height="500" fill="url(#crowd)" role="img" aria-label="Photo of runners leaving the start line on a grassy foreshore course"/>
    <path d="M0,872 Q330,1002 924,770 L924,1200 L0,1200 Z" fill="var(--orange)"/>
    <path d="M0,884 Q330,1012 924,790 L924,1200 L0,1200 Z" fill="var(--white)"/>
    <path d="M0,893 Q330,1022 924,803 L924,1200 L0,1200 Z" fill="url(#lowerBand)"/>
    <rect x="0" y="1127" width="924" height="73" fill="var(--white)"/>
    <path d="M540,1127 L924,1127 L924,1200 L540,1200 L565,1163 Z" fill="var(--orange)"/>
    <path d="M522,1127 L538,1127 L563,1163 L538,1200 L522,1200 L547,1163 Z" fill="var(--navy)"/>
  </svg>

  <div class="abs club-badge">
    <span class="dot"></span>
    <span class="club-name">Pelmora Swifts<br>Stridefair</span>
  </div>

  <h1 class="abs event-title">2018 PELMORA SWIFTS STRIDEFAIR</h1>

  <section class="abs session junior">
    <h3>Junior Stridefair Start</h3>
    <div class="pill"><span class="when">30TH JUNE – 4.00PM</span><span class="day">SATURDAY</span></div>
  </section>
  <div class="abs divider"></div>
  <section class="abs session main">
    <h3>Pelmora Swifts Stridefair</h3>
    <div class="pill"><span class="when">1ST JULY – 7.00AM</span><span class="day">SUNDAY</span></div>
  </section>

  <p class="abs distances" style="margin:0">MARATHON 10KMS | HALF MARATHON 4 KMS</p>

  <div class="abs challenge">
    <span>Strideon<br>team challenge!</span>
    <span class="prize">WIN $1000</span>
    <span>prize money to the<br>charity of your choice</span>
  </div>

  <div class="abs prizes-head">FANTASTIC<span>PRIZES</span></div>
  <div class="abs prizes-rule"></div>
  <ul class="abs prize-list">
    <li>• <b>$4000</b> worth of cash prizes</li>
    <li>• <b>$2000</b> worth of Sports Gear</li>
    <li>• <b>$1000</b> worth of Corvin Hale Jewellery</li>
    <li>(can use logo if prefer in design)</li>
    <li>• All runners awarded awesome</li>
    <li>memento stainless steel water bottle</li>
  </ul>

  <div class="abs footer-sponsors">
    <span class="label">OUR SPONSOR</span>
    <span class="sponsor"><i></i>Pelmora Swifts</span>
    <span class="sponsor">Tallowe</span>
    <span class="sponsor">Kivo Studio</span>
  </div>

  <p class="abs register" style="margin:0">Don’t miss out register at<strong>pelmorastridefair.com</strong></p>
</main>
</body>
</html>
```